依頼詳細
ポリ袋印刷会社様のコーポレートサイトリニューアルに伴うTOPページのデザインをお願いいたします。デザインはPCとスマートフォン両方お願いいたします。
デザインは信頼感があり最新のデザインを取り入れたいと考えております。

現状のサイト
http://www.q-7z.co.jp/

デザインはワイヤーフレームを基に制作をお願いいたします。ワイヤーフレームはあくまで要素を置いているだけなので、レイアウトなどを大幅に変更いただいて構いません。
※ワイヤーフレームは本プロジェクトに添付しております

下記参考サイトのような、シンプルで未来感のあるデザインを希望されております。
https://www.lumo-webplan.co.jp/
https://www.velqor-bix.jp/
https://www.trvn.co.jp/

写真については、一旦素材写真をはめ込んでいただけますでしょうか。

サイトURL
http://www.q-7z.co.jp/
ページ数
2ページ
希望イメージ
シンプル 複雑
単色 カラフル
暗い 明るい
日常 高級
遊び心 厳粛
未来的 伝統的
女性的 男性的
希望する色
青系
納品ファイル
• 高解像度JPG (.jpg)
• フォトショップ形式 (.psd)
■ 選んだ理由

細部まで作り込まれた洗練されたシンプルなデザインがクライアント様のイメージにより近い物だと感じました。

■ 提案者全員のお礼・コメント

お世話になります。
今回はコンペにご参加いただきありがとうございました。またたくさんのご応募ありがとうございました。今回選定できなかったデザイナーの方も、今後もし何かあればご依頼したいと思いますので、引き続きどうぞよろしくお願いいたします。

```html
<!DOCTYPE html>
<html lang="ja">
<head>
<meta charset="utf-8">
<title>株式会社クレストセブン</title>
<link href="https://fonts.googleapis.com/css2?family=Noto+Sans+JP:wght@300;400;500;700&family=Montserrat:wght@300;500;700&display=swap" rel="stylesheet">
<style>
:root{
  --ink:#151515;
  --text:#444;
  --muted:#888;
  --line:#dcdcdc;
  --bg-soft:#f2f2f2;
  --bg-grey:#e4e4e4;
  --dark:#3a3a3a;
  --blue:#2b22c0;
  --navy:#17143d;
  --pink:#f06aa8;
  --white:#fff;
}
*{margin:0;padding:0;box-sizing:border-box}
html,body{width:1200px;height:5292px;overflow:hidden}
body{font-family:"Noto Sans JP",sans-serif;color:var(--ink);background:var(--white);position:relative}
.abs{position:absolute}
.en{font-family:"Montserrat",sans-serif}
.ph{position:absolute}
.header{position:absolute;left:0;top:0;width:1200px;height:62px;display:flex;align-items:center;z-index:5;background:rgba(255,255,255,.9)}
.brand{display:flex;align-items:center;gap:8px;margin-left:22px;font-size:13px;font-weight:700}
.brand i{width:20px;height:20px;background:var(--navy);display:block}
.nav{display:flex;gap:26px;margin-left:auto;margin-right:24px;font-size:11px;font-weight:500}
.nav-cta{width:150px;height:62px;background:var(--pink);color:#fff;font-size:12px;font-weight:700;display:flex;align-items:center;justify-content:center}
.hero-grid{position:absolute;left:0;top:62px;width:1200px;height:560px;display:grid;grid-template-columns:repeat(5,1fr);grid-template-rows:repeat(2,1fr);gap:14px;padding:0 10px;background:#f4f4f4}
.hero-grid div{background:radial-gradient(ellipse at 50% 45%,#ffffff 0%,#f0f0f0 45%,#cfcfcf 100%)}
.hero-copy{left:120px;top:380px;font-size:66px;font-weight:300;letter-spacing:.04em;background:rgba(255,255,255,.82);padding:2px 22px;line-height:1.35}
.hero-lead{left:640px;top:290px;width:300px;font-size:12px;line-height:1.9;background:rgba(255,255,255,.92);padding:10px 16px}
.news{left:600px;top:600px;width:600px;height:62px;background:#fff;display:flex;align-items:center;font-size:12px;z-index:2}
.news .lbl{padding:0 6px 4px;font-weight:700;border-bottom:2px solid var(--ink);margin-left:0}
.news .date{font-size:9px;color:var(--muted);line-height:1.3}
.news .tt{margin-left:24px;color:var(--text)}
.news .more{margin-left:auto;width:130px;height:62px;background:var(--ink);color:#fff;display:flex;align-items:center;justify-content:center;font-size:11px}
.eyebrow{font-size:10px;letter-spacing:.12em;color:var(--blue);font-weight:700}
.h2{font-size:34px;font-weight:400;letter-spacing:.05em;line-height:1.3}
.btn{position:absolute;width:280px;height:58px;background:var(--ink);color:#fff;font-size:12px;display:flex;align-items:center;padding:0 28px;z-index:2}
.btn::after{content:"";margin-left:auto;width:26px;height:1px;background:#fff}
.ghost{position:absolute;font-family:"Montserrat",sans-serif;font-weight:300;font-size:130px;letter-spacing:.06em;color:#ececec;white-space:nowrap;line-height:1}
.body{font-size:12px;line-height:2;color:var(--text)}
.card{position:absolute;width:240px;background:#fff;box-shadow:0 4px 18px rgba(0,0,0,.08);padding:34px 22px 30px;text-align:center;z-index:2}
.card svg{display:block;margin:0 auto 18px}
.card h3{font-size:14px;margin-bottom:14px;font-weight:700}
.card p{font-size:10.5px;line-height:1.9;color:var(--text);text-align:left}
.item{position:absolute;width:180px}
.item .img{height:130px}
.item .lbl{font-size:14px;font-weight:700;margin-top:8px}
.item .sub{font-size:10px;color:var(--muted);line-height:1.6}
.case{position:absolute;width:300px}
.case .img{height:150px;width:190px}
.case .tag{background:var(--blue);color:#fff;font-size:9px;padding:2px 6px;display:inline-block;margin-top:10px}
.case .nm{font-size:16px;font-weight:700;margin-top:2px}
.case p{font-size:10px;line-height:1.7;color:var(--text);margin-top:6px}
.footer{left:0;top:4972px;width:1200px;height:320px;background:var(--navy);color:#fff}
</style>
</head>
<body>

<header class="header">
  <div class="brand"><i></i>株式会社クレストセブン</div>
  <nav class="nav"><span>クレストセブンの強み</span><span>取扱商品</span><span>設備紹介</span><span>導入実績</span><span>会社概要</span></nav>
  <div class="nav-cta">お問い合わせ</div>
</header>

<div class="hero-grid" role="img" aria-label="白い無地のポリ袋を並べた写真">
  <div></div><div></div><div></div><div></div><div></div>
  <div></div><div></div><div></div><div></div><div></div>
</div>
<div class="abs hero-copy">袋のことなら</div>
<p class="abs hero-lead">クレストセブンでは、企画段階から製品化まで、ポリ袋の印刷・加工をワンストップでご提案いたします。</p>
<div class="abs news">
  <span style="margin-left:24px" class="lbl en">NEWS</span>
  <span style="margin-left:22px"><span class="date en">2024.04.01</span><br><b>お知らせ</b></span>
  <span class="tt">ホームページをリニューアルしました。</span>
  <span class="more en">View more&nbsp;&nbsp;—</span>
</div>

<div class="abs" style="left:0;top:680px;width:600px;height:330px;background:var(--dark)"></div>
<div class="abs" style="left:600px;top:1290px;width:600px;height:410px;background:var(--bg-grey)"></div>
<div class="abs" style="left:600px;top:1640px;width:600px;height:60px;background:#aaa"></div>
<div class="abs h2" style="left:600px;top:725px;padding-left:16px;border-left:1px solid var(--line)">クレストセブンの<br>3つの強み</div>
<div class="abs" style="left:616px;top:840px;font-size:13px;font-weight:700"><span style="color:var(--blue)">CS</span>の3つの力</div>
<p class="abs body" style="left:616px;top:870px;width:440px">「環境力」「商品力」「ニーズ力」を軸に、お客様の課題に合わせた最適な提案を行います。</p>

<div class="card" style="left:180px;top:920px">
  <svg width="80" height="80" viewBox="0 0 80 80"><circle cx="40" cy="40" r="36" fill="#8a8a8a"/><path d="M20 30q10-8 18 0t10 12q-6 8-2 18M52 18q6 10 14 12" stroke="#fff" stroke-width="3" fill="none"/></svg>
  <h3>環境対応</h3>
  <p>環境配慮型の素材を積極的に採用し、リサイクル可能なフィルムや植物由来の原料を使用した製品づくりを進めています。</p>
</div>
<div class="card" style="left:180px;top:1370px">
  <svg width="80" height="70" viewBox="0 0 80 70"><rect x="10" y="14" width="60" height="44" fill="none" stroke="#999" stroke-width="2"/><path d="M10 14l30 22 30-22" stroke="#999" stroke-width="2" fill="none"/></svg>
  <h3>商品対応</h3>
  <p>多彩なフィルムと印刷技術を組み合わせ、小ロットから大量生産まで幅広い商品に柔軟に対応しております。</p>
</div>
<div class="card" style="left:540px;top:1370px">
  <svg width="80" height="70" viewBox="0 0 80 70"><circle cx="40" cy="30" r="18" fill="none" stroke="#999" stroke-width="2"/><rect x="33" y="50" width="14" height="10" fill="#999"/><path d="M40 2v6M14 30H8M72 30h-6M20 10l4 4M60 10l-4 4" stroke="#999" stroke-width="2"/></svg>
  <h3>ニーズ対応</h3>
  <p>お客様一人ひとりの声に耳を傾け、企画から納品まで一貫した体制で最適なご提案をいたします。</p>
</div>
<div class="btn" style="left:730px;top:1620px">詳しくはこちら</div>

<div class="ghost" style="left:-10px;top:1720px">CREST SEVEN</div>
<div class="abs" style="left:600px;top:1740px;width:600px;height:1000px;background:var(--bg-soft)"></div>
<div class="ph" style="left:640px;top:1740px;width:560px;height:300px;background:linear-gradient(160deg,#fdfdfd 0%,#e9e9e9 40%,#c4c4c4 70%,#efefef 100%)" role="img" aria-label="重ねた透明ポリ袋の写真"></div>
<div class="abs" style="left:140px;top:1850px"><div class="eyebrow en">PRODUCTS</div><div class="h2" style="font-size:30px;margin-top:4px">取り扱い商品</div></div>
<div class="abs" style="left:140px;top:1960px;font-size:16px;font-weight:700">機能フィルムにプラスワン</div>
<p class="abs body" style="left:140px;top:1994px;width:440px;font-size:11px">独自の機能フィルムにさまざまな加工を加え、用途に合わせた商品を提案いたします。</p>

<div class="item" style="left:140px;top:2090px"><div class="img" style="background:linear-gradient(135deg,#2a2a2a,#6e6e64 50%,#1c1c1c)" role="img" aria-label="発送袋の商品写真"></div><div class="lbl">発送袋関係</div><div class="sub">宅配袋・封筒袋など</div></div>
<div class="item" style="left:330px;top:2090px"><div class="img" style="background:linear-gradient(135deg,#1f1f1f,#7a7f86 55%,#222)" role="img" aria-label="OPP袋の商品写真"></div><div class="lbl">OPP袋関係</div><div class="sub">透明袋・ヘッダー袋など</div></div>
<div class="item" style="left:140px;top:2330px"><div class="img" style="background:linear-gradient(135deg,#e8e6e0,#9aa7b5 50%,#c9b48e)" role="img" aria-label="手提げバッグの商品写真"></div><div class="lbl">バッグ関係</div><div class="sub">手提げ袋・レジ袋など</div></div>
<div class="item" style="left:330px;top:2330px"><div class="img" style="background:linear-gradient(135deg,#3f8fc9,#c95a7a 50%,#5aa66a)" role="img" aria-label="機能袋の商品写真"></div><div class="lbl">機能袋関係</div><div class="sub">帯電防止・防錆袋など</div></div>
<div class="item" style="left:520px;top:2330px"><div class="img" style="background:linear-gradient(135deg,#6b4a2e,#c99a5a 50%,#8b5a3a)" role="img" aria-label="食品袋の商品写真"></div><div class="lbl">食品袋関係</div><div class="sub">食品包装・真空袋など</div></div>
<div class="btn" style="left:730px;top:2400px">詳しくはこちら</div>

<div class="ph" style="left:0;top:2620px;width:1200px;height:480px;background:linear-gradient(100deg,#23252c 0%,#4a4d57 30%,#9aa0aa 60%,#d8dadd 100%)" role="img" aria-label="オフィスで打ち合わせをするスタッフの写真"></div>
<div class="abs" style="left:0;top:2940px;width:160px;height:180px;background:var(--blue)"></div>
<div class="abs" style="left:160px;top:2940px;width:110px;height:140px;background:var(--ink);color:#fff;font-size:11px;font-weight:700;display:flex;align-items:center;justify-content:center;text-align:center;line-height:1.6">お客様の<br>立場に立った<br>開発</div>
<div class="abs" style="left:270px;top:2955px;width:890px;height:120px;background:#fff;border:1px solid var(--line);display:flex;align-items:center;padding:0 30px">
  <div><div style="font-size:18px;font-weight:700">お客様の立場に立った新商品開発</div><p class="body" style="font-size:10.5px;line-height:1.8;margin-top:6px">様々なフィルムや加工技術を組み合わせ、<br>お客様の課題を解決する新しい袋を<br>企画から提案いたします。</p></div>
  <div style="margin-left:auto;display:flex;gap:22px">
    <svg width="56" height="56"><circle cx="28" cy="28" r="26" fill="none" stroke="#999"/><rect x="18" y="18" width="20" height="20" fill="none" stroke="#666"/></svg>
    <svg width="56" height="56"><circle cx="28" cy="28" r="26" fill="none" stroke="#999"/><path d="M18 36l8-12 6 8 6-6" stroke="#666" fill="none"/></svg>
    <svg width="56" height="56"><circle cx="28" cy="28" r="26" fill="none" stroke="#999"/><circle cx="28" cy="26" r="8" fill="none" stroke="#666"/></svg>
  </div>
</div>

<div class="ph" style="left:0;top:3220px;width:1200px;height:660px;background:linear-gradient(120deg,#5a6070 0%,#8d96a8 35%,#c9b76a 55%,#8a909c 75%,#b7bcc5 100%)" role="img" aria-label="倉庫でフォークリフトが荷物を運ぶ写真"></div>
<div class="abs" style="left:540px;top:3290px;width:660px;height:520px;background:#fff;overflow:hidden">
  <div class="ghost" style="left:-20px;top:30px;font-size:110px">CREST SEVEN</div>
</div>
<div class="abs" style="left:580px;top:3300px"><div class="eyebrow en">FACILITY</div><div class="h2" style="font-size:30px;margin-top:4px">設備紹介</div></div>
<div class="abs" style="left:580px;top:3420px;font-size:20px;font-weight:700;line-height:1.6">コストダウン・柔軟な対応を実現する、<br>クレストセブンの一貫した生産体制</div>
<p class="abs body" style="left:580px;top:3510px;width:460px;font-size:11px">製膜から印刷、製袋までを自社工場で一貫して行うことで、品質を保ちながらコストを抑え、短納期にも柔軟にお応えします。最新の設備と熟練の技術で安定した生産を続けています。</p>
<div class="btn" style="left:740px;top:3700px">詳しくはこちら</div>

<div class="abs" style="left:0;top:3960px;width:1200px;height:1012px;background:var(--bg-soft);overflow:hidden">
  <div class="ghost" style="left:0;top:40px;color:#e2e2e2">CREST SEVEN</div>
</div>
<div class="abs" style="left:80px;top:4060px;width:1000px;height:860px;background:#fff"></div>
<div class="abs" style="left:140px;top:4120px"><div class="eyebrow en">USERS CASE</div><div class="h2" style="font-size:30px;margin-top:4px">導入実績</div></div>
<div class="abs" style="left:140px;top:4240px;font-size:16px;font-weight:700">ソリューションのご活用</div>
<p class="abs body" style="left:140px;top:4270px;font-size:11px">幅広い業種のお客様に、課題解決のための袋をご提案しています。</p>

<div class="case" style="left:320px;top:4340px">
  <div class="img" style="margin-left:110px;background:linear-gradient(135deg,#e9ecef,#b9c3cf 60%,#f4f5f7)" role="img" aria-label="イベント会社担当者の写真"></div>
  <span class="tag">イベント</span><div class="nm">イベントプラス</div>
  <p>オリジナル印刷の袋で、イベント会場での配布物の印象が大きく向上しました。</p>
</div>
<div class="case" style="left:720px;top:4340px">
  <div class="img" style="background:linear-gradient(135deg,#dfe3e8,#3b4150 55%,#c9ced6)" role="img" aria-label="観光会社スタッフの写真"></div>
  <span class="tag">観光</span><div class="nm">サクラ観光</div>
  <p>土産物の包装を一新し、ブランドの統一感が生まれたと好評です。</p>
</div>
<div class="case" style="left:320px;top:4600px">
  <div class="img" style="margin-left:110px;background:linear-gradient(135deg,#eef0f2,#9aa3ad 55%,#f2f3f5)" role="img" aria-label="アパレル会社担当者の写真"></div>
  <span class="tag">アパレル</span><div class="nm">アパレルミナト</div>
  <p>ショップ袋の素材を見直し、コストと環境負荷を同時に削減できました。</p>
</div>
<div class="btn" style="left:730px;top:4800px">詳しくはこちら</div>

<div class="abs" style="left:1022px;top:4948px;width:48px;height:48px;background:var(--ink);z-index:3;display:flex;align-items:center;justify-content:center"><svg width="14" height="10"><path d="M1 9l6-7 6 7" stroke="#fff" fill="none" stroke-width="1.5"/></svg></div>

<footer class="abs footer">
  <div class="abs" style="left:40px;top:50px;display:flex;align-items:center;gap:12px;font-size:20px;font-weight:700"><i style="width:30px;height:30px;background:#fff;display:block"></i>株式会社クレストセブン</div>
  <div class="abs" style="left:40px;top:118px;font-size:10px;line-height:1.7;color:#c9c8e0">大阪本社<br>〒556-0000<br>大阪府大阪市浪速区港町1-2-3</div>
  <div class="abs" style="left:230px;top:118px;font-size:10px;line-height:1.7;color:#c9c8e0">東京営業所<br>〒111-0000<br>東京都台東区浅草橋4-5-6</div>
  <div class="abs" style="left:40px;top:182px;font-size:15px;line-height:1.6">TEL 06-6000-1234<br><span style="font-size:11px">FAX 06-6000-1235</span></div>
  <div class="abs" style="left:230px;top:182px;font-size:15px;line-height:1.6">TEL 03-5000-4321<br><span style="font-size:11px">FAX 03-5000-4322</span></div>
  <div class="abs" style="left:560px;top:56px;font-size:11px">✉ info@q-7z.co.jp</div>
  <div class="abs" style="left:900px;top:56px;font-size:10px;line-height:2.3;color:#c9c8e0">クレストセブンの強み<br>取扱商品<br>設備紹介<br>導入実績<br>会社概要</div>
  <div class="abs" style="left:1040px;top:56px;font-size:10px;line-height:2.3;color:#c9c8e0">お知らせ<br>採用情報<br>お問い合わせ<br>個人情報保護方針</div>
  <div class="abs en" style="left:40px;top:290px;font-size:9px;color:#8f8db0">Copyright © Crest Seven Co.,Ltd. All Rights Reserved.</div>
</footer>

</body>
</html>
```